Kitchen Renovation in YOUR area

We need a template for a flyer that we can hand out in neighbourhoods when we're finished renovating a kitchen. Every neighbourhood, we'll swap out a before and after picture to personalize to that neighbourhood. These will be low print run flyers (30-50 each time). We're really hoping that they'll see *their* kitchen in the BEFORE section (since many houses in neighbourhoods are similar) and see what they're kitchen could look like in the AFTER section. So I want the BEFORE and AFTER photos to be easily swapped in and out on my end. I have lots of photos if needed.

Target Market(s)

Home owners looking to have their kitchen's renovated. This is typically in the 35-55 age range. Primarily women.

Colors

Designer to choose colors to be used in the design.

Requirements
Must have
• My logo, a before (0962) and an after (8281) that I can swap out as I go from neighborhood to neighborhood. All the other design elements can be permanent.
• My website address: MaplestoneRemodels.com
Nice to have
• A background of some kitchen work I've done (1171.jpg). I've also included some copy. That copy can change - that's just something I did up quickly. Use what you can and I can make changes later

```html
<!DOCTYPE html>
<html lang="en">
<head>
<meta charset="utf-8">
<title>Kitchen Refacing Flyer – Maplestone Remodels</title>
<link href="https://fonts.googleapis.com/css2?family=Josefin+Sans:wght@400;600&family=Open+Sans:wght@700&display=swap" rel="stylesheet">
<style>
  :root {
    --brand-blue: #1b7fc4;
    --brand-blue-dark: #1a6aa8;
    --ink: #2e2e2e;
    --logo-grey: #5a5a5a;
    --paper: #f2f3f4;
    --frame: #e4e6e8;
    --white: #ffffff;
  }
  * { box-sizing: border-box; margin: 0; padding: 0; }
  html, body { width: 931px; height: 1200px; overflow: hidden; background: var(--paper); }
  .flyer {
    position: relative; width: 931px; height: 1200px; overflow: hidden;
    background: linear-gradient(180deg, #f7f7f8 0%, #eeeff0 100%);
    font-family: Arial, Helvetica, sans-serif; color: var(--ink);
  }
  .hero-photo {
    position: absolute; left: 0; top: 0; width: 931px; height: 560px;
    border-top-left-radius: 170px 120px;
    border-bottom-right-radius: 260px 220px;
    background:
      linear-gradient(100deg, rgba(255,255,255,0) 55%, rgba(255,255,255,.75) 100%),
      linear-gradient(180deg, #d9dadc 0%, #a9abae 38%, #6d7074 55%, #b7b9bc 75%, #d6d7d9 100%);
  }
  .brand {
    position: absolute; left: 604px; top: 128px; width: 280px; text-align: right;
    font-family: "Open Sans", sans-serif; font-weight: 700; color: var(--logo-grey);
    font-size: 44px; line-height: 1;
  }
  .headline {
    position: absolute; left: 37px; top: 340px;
    font-family: "Josefin Sans", sans-serif; color: var(--white); font-weight: 400;
  }
  .headline .lead { font-size: 37px; letter-spacing: 11px; line-height: 48px; }
  .headline .key { font-size: 72px; line-height: 1; margin-top: 10px; letter-spacing: 2px; }
  .intro {
    position: absolute; left: 0; top: 598px; width: 931px; text-align: center;
    font-size: 17px; letter-spacing: 1.6px; word-spacing: 7px; line-height: 20px; color: #333;
  }
  .cta {
    position: absolute; left: 0; top: 640px; width: 931px; text-align: center;
    font-size: 30px; font-weight: 400; letter-spacing: 2px; word-spacing: 10px; color: var(--brand-blue-dark);
  }
  .cta-rule {
    position: absolute; left: 270px; top: 676px; width: 383px; height: 1px;
    background: linear-gradient(90deg, transparent, #8a8d90 30%, #8a8d90 70%, transparent);
  }
  .point {
    position: absolute; left: 16px; width: 389px;
    border-left: 3px solid var(--brand-blue); padding-left: 15px;
    font-size: 14px; line-height: 17px; text-align: justify; color: #333;
  }
  .point em { font-style: normal; color: var(--brand-blue); }
  .shot {
    position: absolute; width: 210px; height: 121px;
    border: 4px solid var(--frame);
    border-radius: 8px 34px 8px 34px;
    box-shadow: 0 1px 3px rgba(0,0,0,.18);
    overflow: hidden;
  }
  .shot .photo {
    width: 100%; height: 100%;
    background: linear-gradient(180deg, #eef0f1 0%, #d8d4ce 45%, #c48a4a 70%, #a8672f 100%);
  }
  .shot.after .photo {
    background: linear-gradient(180deg, #ddd8d2 0%, #c98f55 35%, #4a4a4c 58%, #b2733a 72%, #8b4e24 100%);
  }
  .tag {
    position: absolute; width: 78px; height: 18px;
    background: var(--brand-blue); color: var(--white);
    font-size: 11px; line-height: 18px; text-align: center;
    transform: rotate(-45deg); transform-origin: center;
  }
  .footer {
    position: absolute; left: 0; bottom: 0; width: 931px; height: 37px;
    background: linear-gradient(90deg, var(--brand-blue) 0%, #2a8fd6 60%, var(--brand-blue-dark) 100%);
    display: flex; align-items: center; justify-content: space-between;
    padding: 0 30px 0 38px;
    font-family: "Josefin Sans", sans-serif; color: var(--white);
    font-size: 14px; letter-spacing: 1.5px;
  }
</style>
</head>
<body>
<main class="flyer">
  <div class="hero-photo" role="img" aria-label="Photo of a finished white kitchen with stainless appliances and a mosaic tile backsplash"></div>

  <div class="brand">Maplestone Remodels</div>

  <h1 class="headline">
    <div class="lead">Turn your kitchen into</div>
    <div class="lead">your dream kitchen By</div>
    <div class="key">REFACING!</div>
  </h1>

  <p class="intro">WE'VE JUST COMPLETED A KITCHEN REFACING IN YOUR AREA<br>AND THE RESULTS ARE STUNNING.</p>
  <h2 class="cta">TAKE A LOOK!</h2>
  <div class="cta-rule"></div>

  <p class="point" style="top:740px">A kitchen refacing takes much less time, and costs up to 60% less than a full kitchen renovation. Get the kitchen you always dreamed of without all of the disruption of a full renovation.</p>

  <p class="point" style="top:889px">Refacing is a complete kitchen facelift. Replace the doors (and the out-dated style!), trim, and panels and pick something new and fresh. Make any modifications you'd like (<em>is it time to switch that junk cabinet into a pot-and-pan cabinet?</em>).</p>

  <p class="point" style="top:1037px">Less mess (no need to empty cupboards), less cost (save up to 60% of a typical kitchen renovation), save time (<em>a kitchen refacing typically takes only 3 days</em>!)</p>

  <div class="shot before" style="left:453px;top:720px"><div class="photo" role="img" aria-label="Before photo of a neighbourhood kitchen"></div></div>
  <div class="shot after" style="left:693px;top:720px"><div class="photo" role="img" aria-label="After photo of the refaced kitchen"></div></div>
  <div class="shot before" style="left:453px;top:870px"><div class="photo" role="img" aria-label="Before photo of a neighbourhood kitchen"></div></div>
  <div class="shot after" style="left:693px;top:870px"><div class="photo" role="img" aria-label="After photo of the refaced kitchen"></div></div>
  <div class="shot before" style="left:453px;top:1019px"><div class="photo" role="img" aria-label="Before photo of a neighbourhood kitchen"></div></div>
  <div class="shot after" style="left:693px;top:1019px"><div class="photo" role="img" aria-label="After photo of the refaced kitchen"></div></div>

  <div class="tag" style="left:431px;top:729px">Before</div>
  <div class="tag" style="left:674px;top:729px">After</div>
  <div class="tag" style="left:431px;top:879px">Before</div>
  <div class="tag" style="left:674px;top:879px">After</div>
  <div class="tag" style="left:431px;top:1028px">Before</div>
  <div class="tag" style="left:674px;top:1028px">After</div>

  <footer class="footer">
    <span>519-555-0148</span><span>|</span>
    <span>dana@maplestoneremodels.com</span><span>|</span>
    <span>www.MaplestoneRemodels.com</span>
  </footer>
</main>
</body>
</html>
```